E-Book/ Buch-Cover spannenden Liebesroman gesucht.
Zielgruppe
Ich bin Autorin und suche ein ansprechendes Cover für mein E-Book mit dem Titel:
' Gläserne Sehnsucht'. Es handelt sich um einen spannenden Liebesroman. Die emotionalen Ängste des Protagonisten, stehen neben den offensichtlichen Bedrohungen der Hauptfigur. Beide müssen ihren Weg zu einem Happyend finden. Da der Titel schon etwas „schreit“, sollte das Cover diesen Eindruck eventuell etwas abfedern.
Aufgabenstellung
Kein Kitsch, kein Schnulzencover, es handelt sich bei aller Dramatik trotzdem um einen Liebesroman. Keinen Thriller.

```html
<!DOCTYPE html>
<html lang="de">
<head>
<meta charset="utf-8">
<title>Gläserne Sehnsucht – c. m. sternfeld</title>
<link rel="stylesheet" href="https://fonts.googleapis.com/css2?family=Playfair+Display:wght@400;500&display=swap">
<style>
  :root {
    --sky-top: #0e1a1f;
    --sky-upper: #1f3d45;
    --sky-mid: #4f7c86;
    --sky-low: #93adb3;
    --dusk-rose: #b49a99;
    --dusk-glow: #c9664c;
    --ground: #08080a;
    --ink-light: #ffffff;
    --badge: #0c0c0c;
  }
  html, body {
    margin: 0;
    padding: 0;
    width: 750px;
    height: 1200px;
    overflow: hidden;
    background: var(--ground);
  }
  .cover {
    position: relative;
    width: 750px;
    height: 1200px;
    overflow: hidden;
    font-family: "Playfair Display", "Times New Roman", serif;
    color: var(--ink-light);
  }
  .cover-photo {
    position: absolute;
    inset: 0;
    background: linear-gradient(
      to bottom,
      var(--sky-top) 0%,
      var(--sky-upper) 25%,
      var(--sky-mid) 42%,
      var(--sky-low) 55%,
      var(--dusk-rose) 66%,
      var(--dusk-glow) 73%,
      #3a1f1c 76%,
      var(--ground) 79%,
      var(--ground) 100%
    );
  }
  .title {
    position: absolute;
    left: 0;
    right: 0;
    top: 0;
    margin: 0;
    font-weight: 400;
  }
  .title-line {
    position: absolute;
    white-space: nowrap;
    line-height: 1;
  }
  .title-first {
    top: 118px;
    right: 38px;
    font-size: 92px;
    letter-spacing: -1px;
  }
  .title-main {
    top: 222px;
    left: 30px;
    font-size: 152px;
    letter-spacing: -3px;
  }
  .genre {
    position: absolute;
    top: 536px;
    left: 498px;
    margin: 0;
    font-size: 44px;
    font-weight: 500;
    line-height: 1;
  }
  .author {
    position: absolute;
    left: 0;
    right: 0;
    top: 1022px;
    margin: 0;
    text-align: center;
    font-size: 68px;
    font-weight: 500;
    line-height: 1;
    letter-spacing: -1px;
  }
  .publisher-badge {
    position: absolute;
    left: 688px;
    top: 745px;
    width: 62px;
    height: 114px;
    background: var(--badge);
    display: flex;
    align-items: center;
    justify-content: center;
  }
  .publisher-name {
    font-size: 22px;
    font-weight: 400;
    color: var(--ink-light);
  }
</style>
</head>
<body>
  <main class="cover">
    <div class="cover-photo" role="img" aria-label="Fotografie: Silhouette einer Frau mit wehendem Haar vor einem Abendhimmel in Blau- und Orangetönen, eine Spur leuchtender Lichtpunkte führt zu ihr"></div>

    <h1 class="title">
      <span class="title-line title-first">Gläserne</span>
      <span class="title-line title-main">Sehnsucht</span>
    </h1>

    <p class="genre">roman</p>

    <p class="author">c. m. sternfeld</p>

    <div class="publisher-badge">
      <span class="publisher-name">h&amp;k</span>
    </div>
  </main>
</body>
</html>
```